Corporate flyer introducing a brand new technology apprenticeship program in Australia!

A professional, yet clean and contemporary looking flyer to advertise a brand new service offering in a simple, easy to read format with engaging images. Here is a link to our current online brochure which outlines the program we would like to advertise in a hardcopy flyer/brochure format: https://pages.vendrap.com/Information-on-Technology-Higher-Apprenticeships-for-Employers-Victoria-kT3pzqW7LmRe

Target Market(s)

Medium to large sized businesses involved in using cutting edge technology, such as engineering and advanced manufracturing (3D printing etc)

Industry/Entity Type

Engineering

Colors

Designer to choose colors to be used in the design.

Requirements
Must have
• Contemporary, clean looking, easy to read, tech/engineering/advanced manufacturing related imagery
Nice to have
• Some ideas about different sizes/styles (eg something other than a plain A4 sheet)
Should not have
• Unprofessional or offensive language

```html
<!DOCTYPE html>
<html lang="en">
<head>
<meta charset="utf-8">
<title>Technology Higher Apprentices – Brochure Spreads</title>
<link href="https://fonts.googleapis.com/css2?family=Bebas+Neue&family=Montserrat:wght@500;600;700&family=Nunito+Sans:wght@400;600;700&display=swap" rel="stylesheet">
<style>
  :root{
    --board:#777777;
    --paper:#ffffff;
    --orange:#e6512a;
    --orange-deep:#c9401c;
    --blue:#0b74bb;
    --sky:#b8dcf3;
    --ink:#2b2b2b;
    --grey:#5f5f5f;
    --muted:#a9a9a9;
  }
  *{box-sizing:border-box;margin:0;padding:0}
  html,body{width:1200px;height:1200px;overflow:hidden;background:var(--board)}
  body{position:relative;font-family:"Nunito Sans",Arial,sans-serif;color:var(--ink)}
  .page{position:absolute;width:346px;height:346px;background:var(--paper);
    box-shadow:0 8px 12px rgba(0,0,0,.35);overflow:hidden}
  .page--cover{left:36px;top:225px}
  .page--intro{left:414px;top:225px}
  .page--industry{left:794px;top:225px}
  .page--intake{left:246px;top:634px}
  .page--contact{left:643px;top:634px}
  .abs{position:absolute}

  .brand{position:absolute;display:flex;align-items:center;gap:5px;
    font-family:"Montserrat",sans-serif;font-weight:700;color:var(--orange);
    text-transform:uppercase;letter-spacing:.04em}
  .brand__mark{display:block;background:currentColor}
  .brand--lg{left:20px;top:33px;font-size:10px}
  .brand--lg .brand__mark{width:12px;height:12px}
  .brand--sm{right:26px;top:30px;font-size:5.5px;color:var(--muted)}
  .brand--sm .brand__mark{width:7px;height:7px}

  .body{font-size:4.6px;line-height:1.5;text-align:justify;color:var(--ink)}
  .body p{margin-bottom:4px}

  /* cover */
  .cover__band{right:0;top:0;width:74px;height:346px;background:var(--orange)}
  .cover__photo{left:0;top:83px;width:346px;height:155px;
    background:
      radial-gradient(ellipse 52px 40px at 168px 58px,#ffffff 0 55%,rgba(255,255,255,0) 100%),
      radial-gradient(ellipse 70px 52px at 168px 60px,#2a2a2a 0 78%,rgba(42,42,42,0) 100%),
      radial-gradient(ellipse 40px 30px at 80px 118px,#7fae4a 0 40%,rgba(127,174,74,0) 100%),
      radial-gradient(ellipse 55px 70px at 300px 110px,#fbfbfb 0 50%,rgba(251,251,251,0) 100%),
      linear-gradient(180deg,#ededed 0,#e4e4e4 68%,#f7f7f7 70%,#f2f2f2 100%)}
  .cover__title{left:20px;top:250px;font-family:"Bebas Neue",sans-serif;font-weight:400;font-size:24px;line-height:1.05;letter-spacing:0}
  .cover__title span{display:block}
  .cover__title .t1{color:var(--orange)}
  .cover__title .t2{color:var(--grey)}
  .cover__rule{left:20px;top:302px;width:43px;height:2px;background:var(--orange)}
  .cover__url{left:20px;top:318px;font-size:5.4px;color:var(--ink)}

  /* intro */
  .intro__panel{left:0;top:69px;width:187px;height:193px;background:var(--blue);color:#fff;padding:14px 13px 0 22px}
  .intro__panel h2{font-family:"Montserrat",sans-serif;font-weight:600;font-size:8.4px;white-space:nowrap;margin-bottom:9px}
  .intro__panel h3{font-family:"Montserrat",sans-serif;font-weight:600;font-size:6.6px;white-space:nowrap;margin-bottom:5px}
  .intro__panel .body{color:#fff;font-size:4.5px}
  .intro__rule{left:22px;top:249px;width:44px;height:2px;background:#fff}
  .intro__photo{left:187px;top:69px;width:159px;height:193px;
    background:
      radial-gradient(ellipse 40px 60px at 20px 40px,#e8c9a8 0,rgba(232,201,168,0) 100%),
      radial-gradient(ellipse 60px 40px at 110px 100px,#d7d4cf 0,rgba(215,212,207,0) 100%),
      radial-gradient(ellipse 70px 50px at 40px 150px,#b7814f 0,rgba(183,129,79,0) 100%),
      radial-gradient(ellipse 60px 70px at 150px 170px,#2f7a3c 0,rgba(47,122,60,0) 100%),
      linear-gradient(160deg,#6d5441 0,#3b3129 45%,#3d4a33 75%,#1f5a2f 100%)}

  /* industry */
  .industry__panel{left:14px;top:58px;width:317px;height:149px;background:var(--blue);color:#fff;padding:9px 11px}
  .industry__panel h2{font-family:"Montserrat",sans-serif;font-weight:600;font-size:10px;margin-bottom:6px}
  .industry__panel .body{color:#fff;font-size:4.75px;line-height:1.45}
  .industry__panel .body p{margin-bottom:5px}
  .industry__stages{left:14px;top:207px;width:317px;height:124px;background:var(--sky);
    display:grid;grid-template-columns:repeat(4,1fr);gap:6px;padding:6px 6px 0}
  .stage__art{height:72px;
    background:radial-gradient(ellipse 50% 45% at 50% 60%,#8fa9bd 0,rgba(143,169,189,.35) 55%,rgba(184,220,243,0) 100%)}
  .stage__label{font-size:5.6px;text-align:center;margin:2px 0 3px;color:var(--ink)}
  .stage__note{font-size:3.8px;line-height:1.35;color:var(--ink)}

  /* intake */
  .intake__title{left:20px;top:30px;font-family:"Montserrat",sans-serif;font-weight:600;font-size:9.6px}
  .intake__lead{left:20px;top:49px;width:300px}
  .intake__lead p{margin-bottom:5px}
  .story h4{font-family:"Montserrat",sans-serif;font-weight:600;font-size:5.8px;color:var(--blue);margin-bottom:3px}
  .story .body{font-size:4.8px;line-height:1.45}
  .story--1{left:20px;top:91px;width:148px}
  .story--1b{left:175px;top:100px;width:148px}
  .story--2{left:20px;top:210px;width:148px}
  .story--3{left:180px;top:210px;width:147px}

  /* contact */
  .contact__photo{left:0;top:84px;width:346px;height:168px;
    background:
      radial-gradient(ellipse 90px 50px at 300px 30px,#e9805e 0,rgba(233,128,94,0) 100%),
      radial-gradient(ellipse 120px 60px at 200px 120px,#e06b45 0,rgba(224,107,69,0) 100%),
      radial-gradient(ellipse 80px 50px at 60px 40px,#a9351a 0,rgba(169,53,26,0) 100%),
      linear-gradient(120deg,#bf3e1c,#d4532c 50%,#d9603a)}
  .contact__copy{left:23px;top:116px;width:280px;color:#fff}
  .contact__copy h2{font-family:"Montserrat",sans-serif;font-weight:600;font-size:11px;margin-bottom:10px}
  .contact__copy p{font-family:"Montserrat",sans-serif;font-weight:500;font-size:5.6px;line-height:1.4}
  .contact__details{margin-top:26px}
  .contact__details p{margin-bottom:8px;font-weight:600}
  .contact__rule{left:23px;top:223px;width:40px;height:2px;background:#fff}
</style>
</head>
<body>

<section class="page page--cover">
  <div class="brand brand--lg"><span class="brand__mark"></span>Kestrel Talent</div>
  <div class="abs cover__band"></div>
  <div class="abs cover__photo" role="img" aria-label="Bright studio desk with a computer monitor, desk lamp, potted plant and white file boxes"></div>
  <h1 class="abs cover__title"><span class="t1">Technology Higher</span><span class="t2">Apprentices</span></h1>
  <div class="abs cover__rule"></div>
  <div class="abs cover__url">www.kestrelgroup.com.au</div>
</section>

<section class="page page--intro">
  <div class="brand brand--sm"><span class="brand__mark"></span>Kestrel Talent</div>
  <div class="abs intro__panel">
    <h2>Kestrel Group Talent Solutions</h2>
    <h3>Technology Higher Apprentices Program</h3>
    <div class="body">
      <p>Join industry leaders in this unique program aimed at future proofing Australian businesses.</p>
      <p>The Technology Higher Apprenticeships combine the best of Higher Education and Vocational learning models by training future technicians to a higher skill and knowledge level to meet the needs of an Industry 4.0 based economy.</p>
      <p>These Higher Apprentices are employed in a model similar to a traditional paid apprenticeship while they are also enrolled in a Diploma of Applied Technologies, followed by an Associate Degree covering a range of topics related to emerging technology. The Higher Apprentices will also complete a number of intensive projects where they will commission a cyber-physical system to provide a solution or enhancement for your business. During these projects, the Higher Apprentices will have access to Northvale's world-class Factory of the Future.</p>
    </div>
  </div>
  <div class="abs intro__rule"></div>
  <div class="abs intro__photo" role="img" aria-label="Business people working together at a table with a laptop and tablet"></div>
</section>

<section class="page page--industry">
  <div class="brand brand--sm"><span class="brand__mark"></span>Kestrel Talent</div>
  <div class="abs industry__panel">
    <h2>What is Industry 4.0</h2>
    <div class="body">
      <p>The term Industry 4.0 encompasses the digitalisation of production processes based on devices autonomously communicating with each other along a value chain. Production units become 'smart factories' where computer-driven systems monitor physical processes.</p>
      <p>Automation, sensors, cloud computing, big data analytics and machine-to-machine communication are driving new business opportunities through integration with the global supply chain. Industry 4.0 technologies make it possible to gather and analyse data across machines enabling faster, more flexible, and more efficient processes to produce higher quality goods at reduced costs.</p>
      <p>This in turn increases manufacturing productivity, shifts economics, fosters industrial growth, modifies the profile of the workforce and ultimately changes the competitiveness of companies.</p>
      <p>What does this mean for Australian businesses? Essentially it requires businesses to innovate, collaborate and redefine future parameters. Whilst innovation doesn't necessarily transform an industry overnight, failure to build capability and develop forward thinking infrastructure has the potential to lead to irrelevance much quicker than expected.</p>
    </div>
  </div>
  <div class="abs industry__stages">
    <div class="stage">
      <div class="stage__art" role="img" aria-label="Line illustration of a steam locomotive"></div>
      <div class="stage__label">Industry 1.0</div>
      <div class="stage__note">The Industrial Revolution begins. Mechanisation of manufacturing with the arrival of steam and water power</div>
    </div>
    <div class="stage">
      <div class="stage__art" role="img" aria-label="Line illustration of an early motor car on an assembly line"></div>
      <div class="stage__label">Industry 2.0</div>
      <div class="stage__note">Mass production assembly lines using electrical power</div>
    </div>
    <div class="stage">
      <div class="stage__art" role="img" aria-label="Line illustration of a robotic arm over a conveyor"></div>
      <div class="stage__label">Industry 3.0</div>
      <div class="stage__note">Automated production using electronics, programmable logic controllers (PLC), IT systems and robotics</div>
    </div>
    <div class="stage">
      <div class="stage__art" role="img" aria-label="Line illustration of a connected robot, phone and cloud"></div>
      <div class="stage__label">Industry 4.0</div>
      <div class="stage__note">The 'Smart Factory'. Autonomous decision making of cyber physical systems using machine learning and Big Data analysis. Interoperability through IoT and cloud technology.</div>
    </div>
  </div>
</section>

<section class="page page--intake">
  <div class="brand brand--sm"><span class="brand__mark"></span>Kestrel Talent</div>
  <h2 class="abs intake__title">Current Intake</h2>
  <div class="abs body intake__lead">
    <p>Kestrel Group Talent Solutions has a current 2018 intake of Higher Apprentices who are working towards an Associate Degree in Applied Technologies and working within Kestrel Group member companies, experiencing both on and off-the-job training like never before.</p>
    <p>Here are some examples of their learnings and contributions to date:</p>
  </div>
  <div class="abs story story--1">
    <h4>Story 1: Out of the closet</h4>
    <div class="body"><p>One of the companies had a $60,000 thermal imaging camera sitting in the cupboard collecting dust because they had no time or resources to dedicate towards investigating how to use and calibrate this technology and its software, (which is a rather complex and time consuming process). The Higher Apprentice was given this camera by his Supervisor and told to figure out how to use it with the view to eventually training the senior staff. The Higher Apprentice was also learning about this type of technology as part of his formal qualification. The Higher Apprentice dedicated the next few weeks to learning about this specific camera and was able to provide significant learnings to the business about calibration and use.</p></div>
  </div>
  <div class="abs story story--1b">
    <div class="body"><p>The benefits of knowing how to use this technology will be enormous as the company can use the camera to monitor heat levels of each layer during the 3D printing process which will produce 'real time' data on heat stress, as opposed to the current practice of X-Ray / thermal scanning of welded products. Therefore, the program will provide efficiencies and a return on investment for the camera, as well as saving time in training staff to use the technology.</p></div>
  </div>
  <div class="abs story story--2">
    <h4>Story 2: The missing link</h4>
    <div class="body">
      <p>One of the Industry 4.0 Higher Apprentices saved a company $6,000 by identifying a way to re-purpose a robotic welding nozzle that could replace the current faulty nozzle. The company had placed an order for several new components which would have cost them approximately $6,000.</p>
      <p>This is an ideal example of how Higher Apprenticeships combine technology and practical skills as this Higher Apprentice incorporates use of CAD drawings and looked at the actual machine and identified some missing links. This skill is critical because too often there is a disconnect between what the technical staff are able to articulate in drawings and what the production staff can actually make.</p>
    </div>
  </div>
  <div class="abs story story--3">
    <h4>Story 3: Picture perfect</h4>
    <div class="body"><p>One of the Industry 4.0 Higher Apprentices was asked to come up with CAD drawings of a very large and complex piece of machinery. He produced moving drawings to such a high level that, once completed, they could even be used to train people on how to operate it.</p></div>
  </div>
</section>

<section class="page page--contact">
  <div class="brand brand--lg"><span class="brand__mark"></span>Kestrel Talent</div>
  <div class="abs contact__photo" role="img" aria-label="Orange-tinted photo of hands working over papers at a desk"></div>
  <div class="abs contact__copy">
    <h2>Let's move forward</h2>
    <p>The future is determined by the decisions you make today.<br>Lay a strong foundation for the future success of your business by talking to us about Higher Apprenticeships today.</p>
    <div class="contact__details">
      <p>Email: talent@kestrelgroup.com.au</p>
      <p>Phone: 1300 555 019</p>
    </div>
  </div>
  <div class="abs contact__rule"></div>
</section>

</body>
</html>
```